5 facebook (and instagram) posts for advertising a service of Online Medicine.
This is NOT a facebook page design. This is just facebook (and Instagram) posts design.

We are a medical company providing medicine at distance, using standard videoconsultation and sometimes videoconsultation with a medical device that collects vital signs.

Each post should have:
- Our logo (attached) – if needed it can be just the circular form, but that´s up to you to decide. Ofcourse some design work can be done to this form (watermark, change in dimension, etc)
- Some posts can have the photo of the device (not all the posts because we also provide videoconsultations without the device) – for this please use our website to collect images (https://www.casaorvalhoverde.com/en/kordalix). You can also use the video of the device to collect images (provided as attachment).
- Some stock image at your decision or collected from our website (https://www.casaorvalhoverde.com/pt/medicina-online) or from the provided video (all of these are licensed and you can use them freely – for instance you can collect doctors from our video)
- One or more of the following headlines (please use different headlines for different posts):
 Revolução na Qualidade da Videoconsulta
 O seu Médico com acesso à informação da sua Orrin Wellbook
 Sincronização com Orrin Wellbook
 Possibilidade de usar o dispositivo Kordalix | Medição à Distância de 6 Sinais Vitais
 Revolução na Saúde
 Revolução na Medicina à Distância
 Um Novo Mundo na Saúde
 Segurança e Fiabilidade na Medicina à Distância
 Excelência na Medicina à Distância
 Baixa Médica Online
 Atestados de Saúde
 Renovação de Receituário
 Planos de Monitorização Remota e Acompanhamento Médico desde 10 EUR / Mês

We need 5 posts, all different between each other but where we can feel an aesthetical and graphic/design continuity/coherence of course.
Each post should be provided on adequate format for facebook and Instagram publishing.

Target Market(s)

Patients

Industry/Entity Type

Medicine

Requirements
Must have
• Check description
Nice to have
• Check description

```html
<!DOCTYPE html>
<html lang="pt">
<head>
<meta charset="utf-8">
<title>Casa Orvalho Verde — Posts Medicina Online</title>
<link href="https://fonts.googleapis.com/css2?family=Outfit:wght@400;500;600;700&display=swap" rel="stylesheet">
<style>
:root{
  --blue:#1a9bd0;
  --blue-deep:#0b77a5;
  --ink:#2a2a2c;
  --grey-bg:#e6e7e9;
  --white:#ffffff;
  --device:#17181b;
  --sky:#cfe9f5;
}
*{box-sizing:border-box;margin:0;padding:0}
html,body{width:1200px;height:800px;overflow:hidden;background:var(--grey-bg);font-family:"Outfit",sans-serif;color:var(--ink)}
.board{position:relative;width:1200px;height:800px}
.post{position:absolute;width:308px;height:308px;background:var(--white);overflow:hidden;box-shadow:0 10px 24px rgba(0,0,0,.14)}
.p1{left:90px;top:82px}.p2{left:438px;top:82px}.p3{left:785px;top:82px}
.p4{left:90px;top:427px}.p5{left:438px;top:427px}.p6{left:785px;top:427px}
.photo{position:absolute}
.brand{position:absolute;display:flex;align-items:center;gap:4px}
.brand-dot{width:18px;height:18px;border-radius:50%;background:var(--blue);flex:none}
.brand-name{font-weight:700;color:var(--blue);font-size:11px;line-height:1;letter-spacing:.2px}
.brand-sub{font-weight:400;color:#555;font-size:5px;margin-top:2px}
.headline{position:absolute;font-weight:600;line-height:1.08;letter-spacing:-.3px}
.accent{color:var(--blue)}
.shop{position:absolute;background:var(--blue);color:var(--white);font-weight:600;font-size:8.5px;border-radius:4px;display:flex;align-items:center;justify-content:center}
.dots{position:absolute;display:grid;grid-template-columns:repeat(4,3px);gap:4px}
.dots i{width:3px;height:3px;border-radius:50%;background:var(--blue);display:block}
.url-bar{position:absolute;left:0;top:278px;width:19px;height:9px;background:var(--blue)}
.url{position:absolute;left:26px;top:277px;font-size:7.5px;color:var(--ink)}
.panel{position:absolute;left:218px;width:90px;background:var(--blue);border-radius:0 0 0 14px;color:var(--white)}
.panel.deep{background:var(--blue-deep);border-radius:14px 0 0 14px}
.features{position:absolute;left:8px;list-style:none}
.features li{display:flex;align-items:center;gap:3px;font-size:4.3px;font-weight:600;height:9.2px;white-space:nowrap}
.features svg{width:5px;height:5px;flex:none}
.service{position:absolute;left:8px;display:flex;align-items:flex-end;gap:2px}
.service small{font-size:5px;writing-mode:vertical-rl;transform:rotate(180deg);margin-bottom:3px}
.service b{font-weight:400;font-size:26px;line-height:1}
.device{position:absolute;background:var(--device);border-radius:30px;border:3px solid #dcdcdc}
.center-text{position:absolute;left:0;width:100%;text-align:center;font-weight:500;font-size:16.5px;line-height:1.2;letter-spacing:-.2px}
</style>
</head>
<body>
<main class="board">

  <!-- Post 1 -->
  <section class="post p1">
    <div class="photo" role="img" aria-label="Equipa médica a conversar num escritório luminoso" style="left:90px;top:0;width:218px;height:150px;background:linear-gradient(90deg,rgba(255,255,255,1) 0%,rgba(214,220,226,.9) 45%,#c9d0d8 100%)"></div>
    <div class="brand" style="left:20px;top:29px">
      <span class="brand-dot"></span>
      <div><div class="brand-name">Casa Orvalho Verde</div><div class="brand-sub">Professor Doutor Tomás Regueira</div></div>
    </div>
    <h2 class="headline" style="left:24px;top:114px;font-size:23.5px">Segurança e<br><span class="accent">Fiabilidade</span><br><span class="accent">na Medicina</span> à<br>Distância</h2>
    <div class="panel" style="top:147px;height:143px">
      <ul class="features" style="top:42px">
        <li><svg viewBox="0 0 10 10"><circle cx="5" cy="5" r="4.2" fill="none" stroke="#fff"/><path d="M3 5.2l1.4 1.4L7 4" fill="none" stroke="#fff"/></svg>Frequência Cardíaca</li>
        <li><svg viewBox="0 0 10 10"><circle cx="5" cy="5" r="4.2" fill="none" stroke="#fff"/><path d="M3 5.2l1.4 1.4L7 4" fill="none" stroke="#fff"/></svg>Pressão Arteria</li>
        <li><svg viewBox="0 0 10 10"><circle cx="5" cy="5" r="4.2" fill="none" stroke="#fff"/><path d="M3 5.2l1.4 1.4L7 4" fill="none" stroke="#fff"/></svg>Níveis de Oxigénio no Sangue</li>
        <li><svg viewBox="0 0 10 10"><circle cx="5" cy="5" r="4.2" fill="none" stroke="#fff"/><path d="M3 5.2l1.4 1.4L7 4" fill="none" stroke="#fff"/></svg>Temperatura Corporal</li>
        <li><svg viewBox="0 0 10 10"><circle cx="5" cy="5" r="4.2" fill="none" stroke="#fff"/><path d="M3 5.2l1.4 1.4L7 4" fill="none" stroke="#fff"/></svg>Eletrocardiograma</li>
        <li><svg viewBox="0 0 10 10"><circle cx="5" cy="5" r="4.2" fill="none" stroke="#fff"/><path d="M3 5.2l1.4 1.4L7 4" fill="none" stroke="#fff"/></svg>Açúcar no Sangue</li>
      </ul>
      <div class="service" style="top:106px"><small>Serviço</small><b>24/7</b></div>
    </div>
    <div class="device" role="img" aria-label="Dispositivo Kordalix de medição de sinais vitais" style="left:172px;top:112px;width:112px;height:60px;transform:rotate(8deg)"></div>
    <div class="shop" style="left:25px;top:231px;width:62px;height:18px">SHOP NOW!</div>
    <div class="dots" style="left:156px;top:235px"><i></i><i></i><i></i><i></i><i></i><i></i><i></i><i></i><i></i><i></i><i></i><i></i><i></i><i></i><i></i><i></i></div>
    <span class="url-bar"></span><span class="url">www.casaorvalhoverde.com</span>
  </section>

  <!-- Post 2 -->
  <section class="post p2">
    <div class="photo" role="img" aria-label="Estetoscópio em fundo azul claro" style="left:0;top:0;width:308px;height:150px;background:linear-gradient(180deg,var(--sky) 0%,#e4f3fa 60%,#ffffff 100%)"></div>
    <div class="brand" style="left:20px;top:43px">
      <span class="brand-dot" style="width:24px;height:24px"></span>
      <div><div class="brand-name" style="font-size:13.5px">Casa Orvalho Verde</div><div class="brand-sub" style="font-size:6.5px">Professor Doutor Tomás Regueira</div></div>
    </div>
    <div style="position:absolute;left:183px;top:27px;width:108px;height:92px;border-radius:50%;background:var(--white)"></div>
    <div class="device" role="img" aria-label="Dispositivo Kordalix de medição de sinais vitais" style="left:183px;top:42px;width:86px;height:54px;transform:rotate(12deg)"></div>
    <h2 class="headline" style="left:25px;top:115px;font-size:32px;line-height:1.18"><span class="accent">Um Novo</span><br>Mundo<br><span class="accent">na Saúde</span></h2>
    <div class="dots" style="left:249px;top:135px"><i></i><i></i><i></i><i></i><i></i><i></i><i></i><i></i><i></i><i></i><i></i><i></i></div>
    <ul class="features" style="left:213px;top:199px;color:var(--ink)">
      <li><svg viewBox="0 0 10 10"><circle cx="5" cy="5" r="4.2" fill="none" stroke="#1a9bd0"/><path d="M3 5.2l1.4 1.4L7 4" fill="none" stroke="#1a9bd0"/></svg>Frequência Cardíaca</li>
      <li><svg viewBox="0 0 10 10"><circle cx="5" cy="5" r="4.2" fill="none" stroke="#1a9bd0"/><path d="M3 5.2l1.4 1.4L7 4" fill="none" stroke="#1a9bd0"/></svg>Pressão Arteria</li>
      <li><svg viewBox="0 0 10 10"><circle cx="5" cy="5" r="4.2" fill="none" stroke="#1a9bd0"/><path d="M3 5.2l1.4 1.4L7 4" fill="none" stroke="#1a9bd0"/></svg>Níveis de Oxigénio no Sangue</li>
      <li><svg viewBox="0 0 10 10"><circle cx="5" cy="5" r="4.2" fill="none" stroke="#1a9bd0"/><path d="M3 5.2l1.4 1.4L7 4" fill="none" stroke="#1a9bd0"/></svg>Temperatura Corporal</li>
      <li><svg viewBox="0 0 10 10"><circle cx="5" cy="5" r="4.2" fill="none" stroke="#1a9bd0"/><path d="M3 5.2l1.4 1.4L7 4" fill="none" stroke="#1a9bd0"/></svg>Eletrocardiograma</li>
      <li><svg viewBox="0 0 10 10"><circle cx="5" cy="5" r="4.2" fill="none" stroke="#1a9bd0"/><path d="M3 5.2l1.4 1.4L7 4" fill="none" stroke="#1a9bd0"/></svg>Açúcar no Sangue</li>
    </ul>
    <div style="position:absolute;left:213px;top:258px;width:66px;height:1px;background:#9aa"></div>
    <div class="service" style="left:213px;top:263px;color:var(--blue)"><small style="color:var(--ink)">Serviço</small><b style="font-weight:700;font-size:25px">24/7</b></div>
    <div class="shop" style="left:25px;top:242px;width:62px;height:18px">SHOP NOW!</div>
    <span class="url-bar"></span><span class="url">www.casaorvalhoverde.com</span>
  </section>

  <!-- Post 3 -->
  <section class="post p3" style="background:linear-gradient(160deg,#ffffff 0%,#eceef1 100%)">
    <div class="brand" style="left:93px;top:37px">
      <span class="brand-dot" style="width:26px;height:26px"></span>
      <div><div class="brand-name" style="font-size:12.5px">Casa Orvalho Verde</div><div class="brand-sub" style="font-size:6px">Professor Doutor Tomás Regueira</div></div>
    </div>
    <div class="device" role="img" aria-label="Mão a tocar no ecrã do dispositivo Kordalix" style="left:91px;top:90px;width:127px;height:66px;border-color:var(--device)"></div>
    <div class="photo" role="img" aria-label="Mão a apontar para o ecrã" style="left:140px;top:150px;width:36px;height:52px;border-radius:12px 12px 4px 4px;background:#d9b49a"></div>
    <p class="center-text" style="top:221px">O seu Médico com<br><span class="accent">acessoà informação</span> da<br>sua Orrin Wellbook</p>
  </section>

  <!-- Post 4 -->
  <section class="post p4" style="background:linear-gradient(200deg,#ffffff 0%,#eceef1 100%)">
    <div class="brand" style="left:93px;top:37px">
      <span class="brand-dot" style="width:26px;height:26px"></span>
      <div><div class="brand-name" style="font-size:12.5px">Casa Orvalho Verde</div><div class="brand-sub" style="font-size:6px">Professor Doutor Tomás Regueira</div></div>
    </div>
    <div class="device" role="img" aria-label="Mão a tocar no ecrã do dispositivo Kordalix" style="left:91px;top:90px;width:127px;height:66px;border-color:var(--device)"></div>
    <div class="photo" role="img" aria-label="Mão a apontar para o ecrã" style="left:140px;top:150px;width:36px;height:52px;border-radius:12px 12px 4px 4px;background:#d9b49a"></div>
    <p class="center-text" style="top:221px">O seu Médico com<br><span class="accent">acessoà informação</span> da<br>sua Orrin Wellbook</p>
  </section>

  <!-- Post 5 -->
  <section class="post p5">
    <div class="photo" role="img" aria-label="Médico sorridente de bata branca" style="left:100px;top:0;width:208px;height:150px;background:linear-gradient(90deg,#ffffff 0%,#e2e6ea 40%,#cfd5db 100%)"></div>
    <div class="brand" style="left:20px;top:43px">
      <span class="brand-dot" style="width:24px;height:24px"></span>
      <div><div class="brand-name" style="font-size:13.5px">Casa Orvalho Verde</div><div class="brand-sub" style="font-size:6.5px">Professor Doutor Tomás Regueira</div></div>
    </div>
    <div class="panel" style="top:147px;height:143px">
      <ul class="features" style="top:42px">
        <li><svg viewBox="0 0 10 10"><circle cx="5" cy="5" r="4.2" fill="none" stroke="#fff"/><path d="M3 5.2l1.4 1.4L7 4" fill="none" stroke="#fff"/></svg>Frequência Cardíaca</li>
        <li><svg viewBox="0 0 10 10"><circle cx="5" cy="5" r="4.2" fill="none" stroke="#fff"/><path d="M3 5.2l1.4 1.4L7 4" fill="none" stroke="#fff"/></svg>Pressão Arteria</li>
        <li><svg viewBox="0 0 10 10"><circle cx="5" cy="5" r="4.2" fill="none" stroke="#fff"/><path d="M3 5.2l1.4 1.4L7 4" fill="none" stroke="#fff"/></svg>Níveis de Oxigénio no Sangue</li>
        <li><svg viewBox="0 0 10 10"><circle cx="5" cy="5" r="4.2" fill="none" stroke="#fff"/><path d="M3 5.2l1.4 1.4L7 4" fill="none" stroke="#fff"/></svg>Temperatura Corporal</li>
        <li><svg viewBox="0 0 10 10"><circle cx="5" cy="5" r="4.2" fill="none" stroke="#fff"/><path d="M3 5.2l1.4 1.4L7 4" fill="none" stroke="#fff"/></svg>Eletrocardiograma</li>
        <li><svg viewBox="0 0 10 10"><circle cx="5" cy="5" r="4.2" fill="none" stroke="#fff"/><path d="M3 5.2l1.4 1.4L7 4" fill="none" stroke="#fff"/></svg>Açúcar no Sangue</li>
      </ul>
      <div class="service" style="top:106px"><small>Serviço</small><b>24/7</b></div>
    </div>
    <div class="device" role="img" aria-label="Dispositivo Kordalix de medição de sinais vitais" style="left:166px;top:116px;width:112px;height:60px;transform:rotate(8deg)"></div>
    <h2 class="headline" style="left:23px;top:156px;font-size:28px"><span class="accent">Revolução</span><br>na Saúde</h2>
    <div class="shop" style="left:25px;top:231px;width:62px;height:18px">SHOP NOW!</div>
    <div class="dots" style="left:172px;top:242px"><i></i><i></i><i></i><i></i><i></i><i></i><i></i><i></i><i></i><i></i><i></i><i></i><i></i><i></i><i></i><i></i></div>
    <span class="url-bar"></span><span class="url">www.casaorvalhoverde.com</span>
  </section>

  <!-- Post 6 -->
  <section class="post p6">
    <div class="photo" role="img" aria-label="Médico com auscultadores em videoconsulta" style="left:0;top:0;width:190px;height:160px;background:linear-gradient(90deg,#b9cfe0 0%,#d6e2ec 55%,#ffffff 100%)"></div>
    <div class="dots" style="left:14px;top:17px"><i style="background:#fff"></i><i style="background:#fff"></i><i style="background:#fff"></i><i style="background:#fff"></i><i style="background:#fff"></i><i style="background:#fff"></i><i style="background:#fff"></i><i style="background:#fff"></i><i style="background:#fff"></i><i style="background:#fff"></i><i style="background:#fff"></i><i style="background:#fff"></i></div>
    <div class="brand" style="left:169px;top:32px">
      <span class="brand-dot" style="width:22px;height:22px"></span>
      <div><div class="brand-name" style="font-size:11px">Casa Orvalho Verde</div><div class="brand-sub" style="font-size:5.5px">Professor Doutor Tomás Regueira</div></div>
    </div>
    <div class="panel deep" style="top:83px;height:207px">
      <ul class="features" style="top:105px">
        <li><svg viewBox="0 0 10 10"><circle cx="5" cy="5" r="4.2" fill="none" stroke="#fff"/><path d="M3 5.2l1.4 1.4L7 4" fill="none" stroke="#fff"/></svg>Frequência Cardíaca</li>
        <li><svg viewBox="0 0 10 10"><circle cx="5" cy="5" r="4.2" fill="none" stroke="#fff"/><path d="M3 5.2l1.4 1.4L7 4" fill="none" stroke="#fff"/></svg>Pressão Arteria</li>
        <li><svg viewBox="0 0 10 10"><circle cx="5" cy="5" r="4.2" fill="none" stroke="#fff"/><path d="M3 5.2l1.4 1.4L7 4" fill="none" stroke="#fff"/></svg>Níveis de Oxigénio no Sangue</li>
        <li><svg viewBox="0 0 10 10"><circle cx="5" cy="5" r="4.2" fill="none" stroke="#fff"/><path d="M3 5.2l1.4 1.4L7 4" fill="none" stroke="#fff"/></svg>Temperatura Corporal</li>
        <li><svg viewBox="0 0 10 10"><circle cx="5" cy="5" r="4.2" fill="none" stroke="#fff"/><path d="M3 5.2l1.4 1.4L7 4" fill="none" stroke="#fff"/></svg>Eletrocardiograma</li>
        <li><svg viewBox="0 0 10 10"><circle cx="5" cy="5" r="4.2" fill="none" stroke="#fff"/><path d="M3 5.2l1.4 1.4L7 4" fill="none" stroke="#fff"/></svg>Açúcar no Sangue</li>
      </ul>
      <div style="position:absolute;left:8px;top:166px;width:66px;height:1px;background:rgba(255,255,255,.6)"></div>
      <div class="service" style="top:170px"><small>Serviço</small><b>24/7</b></div>
    </div>
    <div class="device" role="img" aria-label="Dispositivo Kordalix de medição de sinais vitais" style="left:146px;top:96px;width:122px;height:64px;transform:rotate(8deg)"></div>
    <div class="dots" style="left:262px;top:153px"><i style="background:#6fc3e6"></i><i style="background:#6fc3e6"></i><i style="background:#6fc3e6"></i><i style="background:#6fc3e6"></i><i style="background:#6fc3e6"></i><i style="background:#6fc3e6"></i><i style="background:#6fc3e6"></i><i style="background:#6fc3e6"></i><i style="background:#6fc3e6"></i><i style="background:#6fc3e6"></i><i style="background:#6fc3e6"></i><i style="background:#6fc3e6"></i></div>
    <h2 class="headline" style="left:27px;top:155px;font-size:23.5px"><span class="accent">Revolução</span><br>na Qualidade da<br><span class="accent">Videoconsulta</span></h2>
    <div class="shop" style="left:28px;top:245px;width:75px;height:21px;font-size:10px">SHOP NOW!</div>
    <span class="url-bar"></span><span class="url" style="left:30px">www.casaorvalhoverde.com</span>
  </section>

</main>
</body>
</html>
```